Online Book Sale Postcard Design

I need a postcard design to announce the online sale of my paperback book listed on Vorlenta.com and Brindlepress.com. My book is about Christmas and belief in God told in short stories, poems, and prayer to help individuals, children, and families celebrate Christmas.
I live in Houston, TX with my retired parents and younger sister in our neighborhood that has a lot of retired citizens and neighbors. The book is a tribute to the neighborhood which is the source of inspiration for the poem which has the same title as the book "Glowing Windows, Quiet Snowfall." I wrote that poem in 2001 after a car tour of the neighborhood in December of 2000.
This is my first book that I've written and is listed on Vorlenta.com and BrindlePress.com. I have a high resolution cover jpeg upload that I would like to use on the front (full color) of the postcard. The basic information showing when it's for sale and where it can be bought is what I need printed on the postcard. I have marketing copy that can be used, also. I want the postcard to convey joy and cheer to communicate the mood of the season as well as of the book, "Glowing Windows, Quiet Snowfall."
Target Market(s)
Females aged 35+, influenced by husbands and young children, teenagers, and young adults.
Industry/Entity Type
Marketing
Requirements
Nice to have
- I trust your creative judgment. Something that makes homeowners want to keep the postcard for reference and as a reminder to buy for themselves and/or give as a gift.
Should not have
- Don't crowd the postcard with too much information. Specifics is all that's needed. I trust your judgment.

```html
<!DOCTYPE html>
<html lang="en">
<head>
<meta charset="utf-8">
<title>Glowing Windows, Quiet Snowfall – Online Sale Postcard</title>
<link rel="stylesheet" href="https://fonts.googleapis.com/css2?family=Great+Vibes&family=Open+Sans:wght@300;400&display=swap">
<style>
  :root {
    --backdrop: #5e4129;
    --night: #1d110e;
    --night-warm: #2f1a14;
    --maroon: #7a1b22;
    --maroon-deep: #5a1218;
    --sale-red: #e8322e;
    --gold: #f5d67a;
    --cream: #f4e4bd;
    --sand: #ddd2c0;
    --ink: #3a2a25;
    --white: #ffffff;
  }
  * { margin: 0; padding: 0; box-sizing: border-box; }
  html, body { width: 789px; height: 1200px; overflow: hidden; }
  body { background: var(--backdrop); font-family: "Open Sans", sans-serif; position: relative; }

  .postcard { position: absolute; left: 53px; overflow: hidden; }
  .postcard--front { top: 45px; width: 686px; height: 532px;
    background: linear-gradient(160deg, var(--night) 0%, var(--night-warm) 100%); }
  .postcard--back { top: 619px; width: 688px; height: 533px; background: var(--white); }

  .layer { position: absolute; inset: 0; }
  .glow-field { position: absolute; left: 60px; top: 150px; width: 420px; height: 230px;
    background: radial-gradient(ellipse at 55% 50%, rgba(240,170,90,.55) 0%, rgba(200,110,60,.3) 45%, rgba(40,20,15,0) 75%); }

  .headline { position: absolute; left: 58px; top: 38px; font-weight: 300; line-height: 1; }
  .headline__online { display: block; color: var(--gold); font-size: 60px; letter-spacing: 1px; }
  .headline__sale { display: block; color: var(--sale-red); font-size: 92px; margin-top: 2px; }

  .book-title { position: absolute; left: 40px; top: 372px; color: var(--white); font-weight: 300;
    font-size: 36px; line-height: 1.15; }
  .book-title .script { font-family: "Great Vibes", cursive; font-size: 42px; }
  .book-title__line2 { display: block; padding-left: 30px; }
  .where-to-buy { position: absolute; left: 20px; top: 480px; color: var(--gold);
    font-size: 19px; font-weight: 300; letter-spacing: .5px; }

  .book-cover { position: absolute; left: 368px; top: 25px; width: 295px; height: 440px;
    background: radial-gradient(ellipse at 40% 45%, #fffaf0 0%, #efe2c0 55%, #cdb98a 100%);
    box-shadow: 8px 10px 18px rgba(0,0,0,.5); border-right: 14px solid #e9e6e2; }

  .back-panel { position: absolute; left: 0; top: 0; width: 100%; height: 100%; }
  .blurb { position: absolute; left: 27px; top: 38px; width: 250px; color: var(--ink);
    font-size: 14.6px; line-height: 1.25; }
  .blurb p + p { margin-top: 10px; }
  .listing-box { position: absolute; left: 17px; top: 336px; width: 316px; height: 210px;
    background: var(--night-warm); border-radius: 28px 28px 0 0; text-align: center; padding-top: 30px; }
  .listing-box__label { color: var(--cream); font-size: 26px; font-weight: 300; }
  .listing-box__site { color: var(--gold); font-size: 36px; font-weight: 300; line-height: 1.2; display: block; }

  .stamp-box { position: absolute; left: 595px; top: 101px; width: 55px; height: 60px; border: 1.5px solid #222; }
  .address-line { position: absolute; left: 437px; width: 212px; border-top: 1.5px solid #222; }
</style>
</head>
<body>

<section class="postcard postcard--front">
  <div class="glow-field" role="img" aria-label="Soft golden bokeh lights glowing in the dark"></div>
  <svg class="layer" width="686" height="532" viewBox="0 0 686 532" aria-hidden="true">
    <defs>
      <linearGradient id="bandShade" x1="0" y1="0" x2="0" y2="1">
        <stop offset="0" stop-color="#8a2129"/>
        <stop offset="1" stop-color="#5a1218"/>
      </linearGradient>
    </defs>
    <path d="M0,155 C140,230 330,330 686,362 L686,532 L0,532 Z" fill="url(#bandShade)"/>
    <path d="M0,198 C170,270 380,335 686,352" fill="none" stroke="#f4e4bd" stroke-width="2"/>
    <path d="M0,232 C190,300 400,350 686,368" fill="none" stroke="#f4e4bd" stroke-width="1.5"/>
  </svg>

  <h1 class="headline">
    <span class="headline__online">ONLINE</span>
    <span class="headline__sale">SALE</span>
  </h1>

  <div class="book-cover" role="img" aria-label="Book cover of Glowing Windows, Quiet Snowfall by Marla J. Whitcombe, with warm golden sparkling lights"></div>

  <p class="book-title">
    <span class="script">Glowing</span> WINDOWS,<br>
    <span class="book-title__line2"><span class="script">Quiet</span> SNOWFALL</span>
  </p>
  <p class="where-to-buy">ON VORLENTA.COM &amp; BRINDLEPRESS.COM</p>
</section>

<section class="postcard postcard--back">
  <svg class="back-panel" width="688" height="533" viewBox="0 0 688 533" aria-hidden="true">
    <defs>
      <radialGradient id="sandGlow" cx=".35" cy=".45" r=".7">
        <stop offset="0" stop-color="#fbf6ea"/>
        <stop offset="1" stop-color="#d9cdb8"/>
      </radialGradient>
    </defs>
    <path d="M0,0 L290,0 C330,180 340,380 390,533 L0,533 Z" fill="url(#sandGlow)"/>
    <path d="M290,0 C330,180 340,380 390,533 L430,533 C360,380 335,180 310,0 Z" fill="#e9dfcc"/>
    <path d="M270,0 C300,200 320,380 370,533" fill="none" stroke="#7a1b22" stroke-width="2.5"/>
    <path d="M285,0 C320,200 345,390 400,533" fill="none" stroke="#7a1b22" stroke-width="2"/>
  </svg>

  <div class="blurb">
    <p>The book is a tribute to the neighborhood which is the source of inspiration for the poem which has the same title as the book "Glowing Windows, Quiet Snowfall."</p>
    <p>My book is about Christmas and belief in God told in short stories, poems, and prayer to help individuals, children, and families celebrate Christmas.</p>
  </div>

  <div class="listing-box">
    <p class="listing-box__label">LISTED ON</p>
    <span class="listing-box__site">Vorlenta.com</span>
    <span class="listing-box__site">BrindlePress.com</span>
  </div>

  <div class="stamp-box" aria-label="Stamp area"></div>
  <div class="address-line" style="top:284px"></div>
  <div class="address-line" style="top:316px"></div>
  <div class="address-line" style="top:348px"></div>
</section>

</body>
</html>
```